Ironbark & Vale Construction and Developments business cards

A business card with watermark background (construction work)

Home improvement projects
House renovations
Bathroom and kitchen renovations
House extensions
New builds and granny flats

Director Tomas Verhoeven
(Phone number)
tomas@ivkbuilds.com.au
(Instagram logo) ivk_builds

```html
<!DOCTYPE html>
<html lang="en">
<head>
<meta charset="utf-8">
<title>Ironbark &amp; Vale Construction and Developments – Business Cards</title>
<link rel="stylesheet" href="https://fonts.googleapis.com/css2?family=Montserrat:wght@400;600&family=Arimo:wght@400;700&display=swap">
<style>
  :root {
    --backdrop: #e6e6e4;
    --card: #262627;
    --card-edge: #1b1b1c;
    --accent: #2f78c4;
    --ink: #f2f2f2;
    --rule: #cfcfcf;
    --emboss: #3a3a3c;
  }
  * { margin: 0; padding: 0; box-sizing: border-box; }
  html, body { width: 1200px; height: 801px; overflow: hidden; }
  body {
    background: var(--backdrop);
    font-family: "Arimo", Arial, sans-serif;
    position: relative;
  }
  .card {
    position: absolute;
    top: 246px;
    width: 540px;
    height: 309px;
    background: var(--card);
    border-radius: 4px;
    box-shadow: 0 10px 24px rgba(0,0,0,0.22);
    display: flex;
    align-items: center;
    color: var(--ink);
  }
  .card--front { left: 40px; }
  .card--back { left: 620px; }

  .brand {
    width: 260px;
    padding-left: 34px;
    display: flex;
    align-items: center;
    gap: 12px;
  }
  .brand__mark {
    width: 18px;
    height: 18px;
    flex: none;
    background: var(--accent);
  }
  .brand__name {
    font-family: "Montserrat", sans-serif;
    font-weight: 600;
    font-size: 17px;
    line-height: 1.3;
    color: var(--ink);
  }
  .card--back .brand__mark { background: var(--emboss); }
  .card--back .brand__name { color: var(--emboss); }

  .divider {
    width: 1px;
    height: 132px;
    background: var(--rule);
    flex: none;
  }

  .contact { padding-left: 26px; }
  .contact__name {
    font-weight: 700;
    font-size: 21px;
    color: var(--accent);
  }
  .contact__role {
    font-size: 13px;
    margin-top: 2px;
    margin-bottom: 18px;
  }
  .contact__list { list-style: none; }
  .contact__item {
    display: flex;
    align-items: center;
    gap: 9px;
    font-size: 13px;
    line-height: 21px;
  }
  .contact__icon { width: 13px; height: 13px; flex: none; }

  .services {
    list-style: none;
    padding-left: 22px;
  }
  .services__item {
    font-size: 15px;
    line-height: 26px;
  }
  .services__item::before {
    content: "•";
    margin-right: 6px;
  }
</style>
</head>
<body>

<section class="card card--front" aria-label="Business card front">
  <div class="brand">
    <span class="brand__mark"></span>
    <span class="brand__name">Ironbark &amp; Vale Construction and Developments</span>
  </div>
  <span class="divider"></span>
  <div class="contact">
    <h1 class="contact__name">Tomas Verhoeven</h1>
    <p class="contact__role">Director</p>
    <ul class="contact__list">
      <li class="contact__item">
        <svg class="contact__icon" viewBox="0 0 16 16" aria-hidden="true"><path fill="#2f78c4" d="M3.6 1.2l2.2 2.6c.3.4.3.9 0 1.2L4.7 6.2c.9 2 2.5 3.6 4.5 4.5l1.2-1.1c.3-.3.9-.3 1.2 0l2.6 2.2c.4.3.4.9.1 1.3l-1.2 1.4c-.5.5-1.2.7-1.9.4C6.1 13.2 2.8 9.9 1.1 4.8.8 4.1 1 3.4 1.5 2.9L2.3 1.2c.4-.4 1-.4 1.3 0z"/></svg>
        <span>555-018-2741</span>
      </li>
      <li class="contact__item">
        <svg class="contact__icon" viewBox="0 0 16 16" aria-hidden="true"><rect x="1" y="3" width="14" height="10" fill="#2f78c4"/><path d="M1.5 3.5L8 9l6.5-5.5" fill="none" stroke="#262627" stroke-width="1.4"/></svg>
        <span>tomas@ivkbuilds.com.au</span>
      </li>
      <li class="contact__item">
        <svg class="contact__icon" viewBox="0 0 16 16" aria-hidden="true"><circle cx="8" cy="8" r="6.5" fill="#2f78c4"/></svg>
        <span>ivk_builds</span>
      </li>
    </ul>
  </div>
</section>

<section class="card card--back" aria-label="Business card back">
  <div class="brand">
    <span class="brand__mark"></span>
    <span class="brand__name">Ironbark &amp; Vale Construction and Developments</span>
  </div>
  <span class="divider"></span>
  <ul class="services">
    <li class="services__item">Home improvement projects</li>
    <li class="services__item">House renovations</li>
    <li class="services__item">Bathroom and kitchen renovations</li>
    <li class="services__item">House extensions</li>
    <li class="services__item">New builds and granny flats</li>
  </ul>
</section>

</body>
</html>
```